Design some Business Cards for Varno

Thanks to everyone for their efforts. I will just be reviewing the first two entries from each contestant, so I'd suggest withdrawing entries which are not your favorites & going with your best two. Many thanks, Gareth

I was after a double sided business card for varno.com.au. Varno is a billing app and website for tradesman and service providers who move from site to site.

Firstly design for Gareth Pimm with mobile 0412 555 806 & email demo@varno.com.au.

Logo is attached, so please work with those colours. I've also included our url if you believe that is worth building in.

I would like the original working files and the business card will need to be produced for 3 different employees when the winner is selected.

Additional VARNO text files if this helps.

```html
<!DOCTYPE html>
<html lang="en">
<head>
<meta charset="utf-8">
<title>Varno business card, front and back</title>
<link rel="stylesheet" href="https://fonts.googleapis.com/css2?family=Open+Sans:wght@400;600;700&display=swap">
<style>
  :root {
    --bg: #e9e6e2;
    --card: #fbfbfb;
    --red: #d3222a;
    --ink: #1b1b1b;
    --mark-blue: #1f78c8;
    --name-blue: #2f3f9c;
    --muted: #3a3a3a;
  }
  * { box-sizing: border-box; margin: 0; padding: 0; }
  html, body { width: 1200px; height: 912px; overflow: hidden; }
  body {
    background: var(--bg);
    font-family: "Open Sans", Arial, sans-serif;
    color: var(--ink);
    position: relative;
  }
  .card {
    position: absolute;
    left: 250px;
    width: 700px;
    height: 400px;
    background: var(--card);
    overflow: hidden;
    box-shadow: 0 6px 18px rgba(0,0,0,.18);
  }
  .card--front { top: 37px; }
  .card--back { top: 474px; }
  .card__bands { position: absolute; inset: 0; width: 700px; height: 400px; }

  .brand { position: absolute; display: flex; align-items: center; }
  .brand__dot {
    border-radius: 50%;
    background: var(--mark-blue);
    flex: none;
  }
  .brand__name {
    font-weight: 700;
    color: var(--ink);
    letter-spacing: 3px;
    line-height: 1;
    white-space: nowrap;
  }

  .card--front .brand { left: 178px; top: 148px; }
  .card--front .brand__dot { width: 70px; height: 70px; margin-right: 18px; }
  .card--front .brand__name { font-size: 56px; }
  .front__url {
    position: absolute;
    left: 268px;
    top: 214px;
    font-weight: 700;
    font-size: 18px;
    letter-spacing: 0.5px;
    color: var(--red);
    white-space: nowrap;
  }

  .card--back .brand { left: 282px; top: 52px; }
  .card--back .brand__dot { width: 62px; height: 62px; margin-right: 16px; }
  .card--back .brand__name { font-size: 52px; }

  .person { position: absolute; left: 175px; top: 222px; }
  .person__name { font-size: 27px; font-weight: 400; color: var(--name-blue); line-height: 1.1; white-space: nowrap; }
  .person__role { font-size: 13px; color: var(--muted); margin: 6px 0 0 24px; }
  .contacts { list-style: none; margin-top: 16px; }
  .contacts li {
    display: flex; align-items: center;
    font-size: 14px; color: var(--muted);
    height: 24px;
    white-space: nowrap;
  }
  .contacts svg { width: 16px; height: 16px; margin-right: 12px; flex: none; }
</style>
</head>
<body>

<section class="card card--front" aria-label="Card front">
  <svg class="card__bands" viewBox="0 0 700 400" aria-hidden="true">
    <polygon points="95,0 185,0 5,400 -85,400" fill="var(--red)"/>
    <line x1="118" y1="0" x2="-62" y2="400" stroke="#fff" stroke-width="2"/>
    <line x1="205" y1="0" x2="25" y2="400" stroke="var(--red)" stroke-width="2"/>
    <line x1="218" y1="0" x2="38" y2="400" stroke="var(--red)" stroke-width="2"/>
    <polygon points="640,0 730,0 550,400 460,400" fill="var(--red)"/>
    <line x1="707" y1="0" x2="527" y2="400" stroke="#fff" stroke-width="2"/>
    <line x1="620" y1="0" x2="440" y2="400" stroke="var(--red)" stroke-width="2"/>
    <line x1="607" y1="0" x2="427" y2="400" stroke="var(--red)" stroke-width="2"/>
  </svg>
  <div class="brand">
    <span class="brand__dot"></span>
    <span class="brand__name">VARNO</span>
  </div>
  <p class="front__url">WWW.VARNO.COM.AU</p>
</section>

<section class="card card--back" aria-label="Card back">
  <svg class="card__bands" viewBox="0 0 700 400" aria-hidden="true">
    <polygon points="150,0 240,0 50,400 -40,400" fill="var(--red)"/>
    <line x1="173" y1="0" x2="-17" y2="400" stroke="#fff" stroke-width="2"/>
    <line x1="130" y1="0" x2="-60" y2="400" stroke="var(--red)" stroke-width="2"/>
    <line x1="254" y1="0" x2="64" y2="400" stroke="var(--red)" stroke-width="2"/>
    <polygon points="650,0 740,0 560,400 470,400" fill="var(--red)"/>
    <line x1="717" y1="0" x2="537" y2="400" stroke="#fff" stroke-width="2"/>
    <line x1="630" y1="0" x2="450" y2="400" stroke="var(--red)" stroke-width="2"/>
    <line x1="617" y1="0" x2="437" y2="400" stroke="var(--red)" stroke-width="2"/>
  </svg>
  <div class="brand">
    <span class="brand__dot"></span>
    <span class="brand__name">VARNO</span>
  </div>
  <div class="person">
    <h1 class="person__name">Gareth Pimm</h1>
    <p class="person__role">Managing Director</p>
    <ul class="contacts">
      <li>
        <svg viewBox="0 0 16 16" aria-hidden="true"><circle cx="8" cy="8" r="8" fill="var(--name-blue)"/><rect x="5.5" y="3.5" width="5" height="9" rx="1" fill="none" stroke="#fff" stroke-width="1.2"/></svg>
        0412 555 806
      </li>
      <li>
        <svg viewBox="0 0 16 16" aria-hidden="true"><circle cx="8" cy="8" r="8" fill="var(--name-blue)"/><rect x="4" y="5" width="8" height="6" fill="none" stroke="#fff" stroke-width="1.1"/><polyline points="4,5 8,8.5 12,5" fill="none" stroke="#fff" stroke-width="1.1"/></svg>
        demo@varno.com.au
      </li>
      <li>
        <svg viewBox="0 0 16 16" aria-hidden="true"><circle cx="8" cy="8" r="8" fill="var(--name-blue)"/><circle cx="8" cy="8" r="4.2" fill="none" stroke="#fff" stroke-width="1.1"/><line x1="3.8" y1="8" x2="12.2" y2="8" stroke="#fff" stroke-width="1"/><ellipse cx="8" cy="8" rx="1.8" ry="4.2" fill="none" stroke="#fff" stroke-width="1"/></svg>
        www.varno.com.au
      </li>
    </ul>
  </div>
</section>

</body>
</html>
```